POOL BUILDING CONTRACTOR

our company has shifter focus over the past 18 month we no longer have a retail store and no longer clean pools we build concrete pools. our website if 5 years old we need a completely new site that shows our core product, building concrete pools & renovate concrete pools

here is a few of our competitors;
brantelwaters.com
okvimbuilders.com
ridgeviewlagoonworks.com
plunvora.com
halvertonbasinsandtubs.com
dremblewaterne.com

one we land on a final design I will upload customer before and after photos and any other content needed

Target Market(s)

People looking to build or renovate there pool

Industry/Entity Type

swimming pool

Coding

Coded - Design and coding required

Number of Pages Required

5+ page

Colors
0054AA
0677BA
7BADD7
CADEEF
E8F1F8

Requirements
Must have
• financing Service-Repairs & liners new build-photos renovate-remodeling design-consult customer-reviews Gallery Before-After Contact us 3D Design & Modeling construction process & Timeline Equipment Features Hardscapes I like these sites https://meadowlarkbasinsbycraft.com/ https://holtbergwaters.com/

```html
<!DOCTYPE html>
<html lang="en">
<head>
<meta charset="utf-8">
<title>Tidewell — Concrete Pool Builders</title>
<link href="https://fonts.googleapis.com/css2?family=Poppins:ital,wght@0,300;0,400;0,500;0,600;0,700;1,400&display=swap" rel="stylesheet">
<style>
:root{
  --ink:#3b4b68;
  --ink-soft:#6b778c;
  --slate:#5a7096;
  --slate-dark:#4c6189;
  --cyan:#17b4e6;
  --topbar:#373c48;
  --box:#e9edf2;
  --white:#fff;
}
*{box-sizing:border-box;margin:0;padding:0}
html,body{width:1200px;height:4669px;overflow:hidden;background:#fff}
body{font-family:'Poppins',sans-serif;color:var(--ink);position:relative}
.abs{position:absolute}
a{color:inherit;text-decoration:none}

.topbar{left:0;top:0;width:1200px;height:31px;background:var(--topbar);color:#cfd4dd;font-size:8px;display:flex;justify-content:flex-end;align-items:center;gap:30px;padding-right:142px}
.topbar b{color:#fff;font-weight:600}
.topbar span{display:flex;align-items:center;gap:6px}
.header{left:0;top:31px;width:1200px;height:81px;background:#fff}
.brand{display:flex;align-items:center;gap:8px}
.brand .mark{width:30px;height:30px;border:2px solid var(--slate);background:var(--cyan)}
.brand .name{font-size:30px;font-weight:700;color:var(--slate);line-height:1}
.brand .tag{font-size:7px;color:var(--slate);letter-spacing:.3px}
.nav{left:367px;top:69px;display:flex;font-size:9px;font-weight:500;color:var(--ink)}
.nav a{margin-right:32px}
.call{left:875px;top:57px;display:flex;align-items:center;gap:10px}
.call .ic{width:28px;height:28px;border:1.5px solid var(--cyan);border-radius:50%;display:flex;align-items:center;justify-content:center}
.call small{display:block;font-size:8px;color:var(--ink-soft)}
.call strong{font-size:13px;font-weight:600;color:var(--slate)}

.hero{left:0;top:112px;width:1200px;height:553px;background:linear-gradient(180deg,#8fb3a0 0%,#5f8f78 28%,#2c8fc0 55%,#1f6fa8 75%,#6a5a4d 100%)}
.hero-kicker{left:145px;top:308px;background:var(--slate-dark);color:#fff;font-size:28px;padding:0 20px;height:40px;line-height:40px}
.hero-title{left:145px;top:348px;background:rgba(80,104,145,.85);color:#fff;font-size:57px;font-weight:700;padding:0 22px;height:66px;line-height:66px}

.svc{background:#fff;width:226px;height:254px;top:613px;border-radius:22px 22px 0 0;box-shadow:0 12px 30px rgba(40,60,100,.08);text-align:center;padding-top:45px}
.svc.mid{background:var(--slate);top:586px;height:281px;border-radius:0}
.svc .ico{width:62px;height:62px;border-radius:8px;background:var(--cyan);margin:0 auto 22px;display:flex;align-items:center;justify-content:center}
.svc h3{font-size:18px;font-weight:400;line-height:25px;color:var(--ink)}
.svc.mid h3{color:#fff}
.svc p{font-size:9.5px;line-height:16px;color:var(--ink-soft);margin:14px auto 0;width:180px}
.svc.mid p{color:#e7ecf4}

.reno-panel{left:531px;top:977px;width:524px;height:448px;background:var(--slate)}
.reno-text{left:729px;top:1087px;width:290px;color:#fff}
.reno-text .kick{font-size:10px;color:var(--cyan)}
.reno-text h2{font-size:25px;font-weight:600;line-height:30px;margin-top:8px}
.reno-text p{font-size:9.5px;line-height:16px;color:#e4e9f2;margin-top:10px}
.reno-arrows{left:727px;top:1271px;display:flex;gap:12px}
.reno-arrows span{width:28px;height:28px;border-radius:50%;display:flex;align-items:center;justify-content:center;background:#fff}
.reno-arrows span.on{background:var(--cyan)}
.rcard{top:1057px;height:288px;background:#fff;border-radius:0 0 28px 28px;box-shadow:0 12px 30px rgba(40,60,100,.12);overflow:hidden}
.rcard .ph{height:190px}
.rcard .badge{position:absolute;top:156px;width:72px;height:72px;border-radius:50%;background:var(--cyan);border:4px solid #fff;display:flex;align-items:center;justify-content:center}
.rcard .lbl{position:absolute;bottom:30px;font-size:19px;color:var(--ink);white-space:nowrap}
.rcard .back{position:absolute;bottom:36px;left:18px}

.wash{left:0;top:1450px;width:1200px;height:620px;background:linear-gradient(180deg,#fff 0%,#f3f5f8 60%,#fff 100%)}
.tab{top:1532px;width:290px;height:62px;background:#fff;box-shadow:0 10px 24px rgba(40,60,100,.08);border-radius:0 22px 0 22px;text-align:center;line-height:68px;font-size:15px;color:var(--ink)}
.tab.on{background:var(--cyan);color:#fff}
.tab .num{position:absolute;left:125px;top:-24px;width:40px;height:40px;border-radius:50%;background:var(--cyan);color:#fff;font-size:14px;line-height:40px;font-weight:500}
.tab.on .num{background:var(--slate)}
.center{left:0;width:1200px;text-align:center}
.kick-c{font-size:12px;color:var(--slate)}
.h-sec{font-size:24px;font-weight:500;color:var(--ink)}
.fbox{width:290px;height:140px;background:var(--box);padding:30px 30px 0 30px;overflow:hidden}
.fbox .big{position:absolute;left:12px;top:-4px;font-size:110px;font-weight:700;color:rgba(120,140,170,.10);line-height:1}
.fbox h4{position:relative;font-size:11.5px;font-weight:600;color:var(--slate);line-height:13px}
.fbox p{position:relative;font-size:9.5px;line-height:16px;color:var(--ink-soft);margin-top:10px}

.proj{left:0;top:2125px;width:1200px;height:691px;background:linear-gradient(160deg,#5d7499 0%,#4f6891 50%,#5a7299 100%)}
.filters{left:0;top:2292px;width:1200px;display:flex;justify-content:center;gap:40px;font-size:10.5px;color:#fff}
.filters span{padding:4px 16px}
.filters span.on{background:var(--cyan)}
.pcard{overflow:hidden;color:#fff}
.pcard .shade{position:absolute;left:0;right:0;bottom:0;height:62%;background:linear-gradient(180deg,rgba(23,180,230,0) 0%,rgba(23,180,230,.75) 45%,#17b4e6 100%)}
.pcard .txt{position:absolute;left:22px;bottom:28px;width:260px}
.pcard small{font-size:11px}
.pcard h5{font-size:17px;font-weight:700;line-height:21px;margin-top:6px}
.pcard .price{font-size:30px;font-weight:700;margin-top:8px}
.pcard .arr{position:absolute;right:24px;bottom:36px}

.tcard{left:392px;top:2973px;width:371px;height:296px;background:#fff;border-radius:0 0 50px 0;box-shadow:0 16px 40px rgba(40,60,100,.14);padding:64px 46px 0 46px}
.tcard h3{font-size:25px;font-weight:600;color:var(--ink)}
.tcard p{font-size:12px;font-style:italic;line-height:20px;color:var(--ink-soft);margin-top:18px}
.tcard .who{font-size:10px;font-style:italic;color:var(--ink-soft);margin-top:28px}
.tcard .who b{color:var(--cyan);font-weight:600}
.qmark{left:625px;top:2940px;z-index:2}
.tside{left:803px;top:3031px}
.tside small{font-size:11px;color:var(--slate)}
.tside h2{font-size:25px;font-weight:500;line-height:30px;color:var(--ink);margin-top:12px}
.dots{left:808px;top:3196px;display:flex;gap:18px;align-items:center}
.dots i{width:4px;height:4px;border-radius:50%;background:#c8d0dc;display:block}
.dots i.on{width:8px;height:8px;background:var(--cyan)}

.stat{width:200px}
.stat .circ{width:89px;height:89px;border-radius:50%;background:var(--slate);color:#fff;font-size:30px;font-weight:500;display:flex;align-items:center;justify-content:center}
.stat h6{font-size:12px;font-weight:500;margin-top:14px;color:var(--ink)}
.stat p{font-size:9.5px;line-height:16px;color:var(--ink-soft);margin-top:6px}
.quote{left:687px;top:3437px;width:368px;height:512px;background:#fff;border-radius:0 0 50px 0;box-shadow:0 16px 40px rgba(40,60,100,.12);padding:32px 45px}
.quote h2{font-size:30px;font-weight:600;color:var(--ink)}
.quote h2 em{font-style:normal;color:var(--cyan)}
.field{position:absolute;height:32px;background:#f3f5f8;font-size:9px;color:#9aa4b4;line-height:32px;padding-left:14px}
.submit{position:absolute;left:45px;top:399px;width:138px;height:33px;background:var(--cyan);color:#fff;font-size:11px;font-weight:600;line-height:33px;text-align:center}

.lead{font-size:10.5px;line-height:17px;color:var(--ink-soft);width:460px;margin:0 auto}
.cta-phone{left:0;top:4194px;width:1200px;display:flex;justify-content:center;align-items:center;gap:10px;font-size:15px;font-weight:600;color:var(--slate)}

.footer{left:0;top:4318px;width:1200px;height:351px;background:linear-gradient(180deg,#536b92,#4e668e)}
.ftab{left:451px;top:4318px;width:298px;height:73px;background:#fff;border-radius:0 0 28px 28px;display:flex;justify-content:center;align-items:center}
.fcol{color:#fff}
.fcol h4{font-size:14px;font-weight:600}
.fcol p{font-size:9.5px;line-height:17px;color:#e4e9f2;margin-top:16px}
.flinks{font-size:9.5px;color:#e4e9f2;line-height:25px}
.flinks div::before{content:"›";margin-right:8px;color:var(--cyan)}
.soc{width:26px;height:26px;border:1.5px solid #fff;border-radius:50%}
.fcontact{font-size:9.5px;line-height:25px;font-weight:600;margin-top:10px}
.copy{left:0;top:4635px;width:1200px;text-align:center;font-size:9.5px;color:#e4e9f2}
</style>
</head>
<body>

<div class="abs topbar">
  <span><svg width="9" height="11" viewBox="0 0 9 11"><path d="M4.5 0C2 0 0 2 0 4.4 0 7.5 4.5 11 4.5 11S9 7.5 9 4.4C9 2 7 0 4.5 0z" fill="#17b4e6"/><circle cx="4.5" cy="4.3" r="1.6" fill="#373c48"/></svg><b>1270 Larkspur Lane Fairview, VA</b></span>
  <span><svg width="10" height="10" viewBox="0 0 10 10"><circle cx="5" cy="5" r="4.2" fill="none" stroke="#17b4e6"/><path d="M5 2.5V5h2" stroke="#17b4e6" fill="none"/></svg>Working Time: <b>Mon - Sat · Free Design Consults</b></span>
</div>

<header class="abs header">
  <div class="abs brand" style="left:145px;top:20px">
    <div class="mark"></div>
    <div><div class="name">Tidewell</div><div class="tag">CONCRETE POOL BUILDERS</div></div>
  </div>
</header>
<nav class="abs nav"><a>Home</a><a>About</a><a>Builds</a><a>Remodel</a><a>Gallery</a><a>Financing</a><a>Reviews</a><a>Contacts</a><a>|</a></nav>
<div class="abs call">
  <div class="ic"><svg width="14" height="14" viewBox="0 0 24 24"><path d="M6.6 10.8a15 15 0 006.6 6.6l2.2-2.2a1 1 0 011-.25 11.4 11.4 0 003.6.6 1 1 0 011 1V20a1 1 0 01-1 1A17 17 0 013 4a1 1 0 011-1h3.5a1 1 0 011 1c0 1.25.2 2.45.6 3.6a1 1 0 01-.25 1z" fill="none" stroke="#17b4e6" stroke-width="1.6"/></svg></div>
  <div><small>Call Now!</small><strong>0-(800)-555-01-42</strong></div>
</div>

<section class="abs hero" role="img" aria-label="Custom concrete pool with blue water, loungers and palm trees on a wooden deck"></section>
<div class="abs hero-kicker">Reach Out for a</div>
<h1 class="abs hero-title">Pristine Pool Experience</h1>

<article class="abs svc" style="left:261px">
  <div class="ico"><svg width="26" height="26" viewBox="0 0 26 26" fill="none" stroke="#fff" stroke-width="1.6"><rect x="4" y="9" width="18" height="12"/><path d="M4 15h18M9 9V5h8v4"/></svg></div>
  <h3>Concrete Pool<br>Construction</h3>
  <p>Custom gunite pools engineered, shaped and built from the ground up.</p>
</article>
<article class="abs svc mid" style="left:487px">
  <div class="ico"><svg width="28" height="28" viewBox="0 0 28 28" fill="none" stroke="#fff" stroke-width="1.6"><circle cx="14" cy="5" r="2.5"/><rect x="6" y="10" width="16" height="9"/><path d="M3 22c2-1.5 4-1.5 5.5 0s4 1.5 5.5 0 4-1.5 5.5 0 4 1.5 5.5 0"/></svg></div>
  <h3>Pool Renovation<br>&amp; Remodeling</h3>
  <p>Resurfacing, new tile, coping and equipment for tired concrete pools.</p>
</article>
<article class="abs svc" style="left:713px">
  <div class="ico"><svg width="26" height="26" viewBox="0 0 26 26" fill="none" stroke="#fff" stroke-width="1.6"><path d="M13 3l9 5v10l-9 5-9-5V8z"/><path d="M4 8l9 5 9-5M13 13v10"/></svg></div>
  <h3>3D Design<br>&amp; Modeling</h3>
  <p>See your pool, spa and hardscape in 3D before we break ground.</p>
</article>

<div class="abs reno-panel"></div>
<div class="abs reno-text">
  <div class="kick">Our pool renovations</div>
  <h2>Our Expert<br>Renovation Services</h2>
  <p>Every pool is distinct. We resurface, retile and remodel concrete pools, replace liners and repair leaks, and upgrade equipment and hardscapes to match your yard. Browse our before and after gallery.</p>
</div>
<div class="abs reno-arrows">
  <span><svg width="10" height="10" viewBox="0 0 10 10"><path d="M6.5 1.5L3 5l3.5 3.5" stroke="#3b4b68" stroke-width="1.5" fill="none"/></svg></span>
  <span class="on"><svg width="10" height="10" viewBox="0 0 10 10"><path d="M3.5 1.5L7 5 3.5 8.5" stroke="#fff" stroke-width="1.5" fill="none"/></svg></span>
</div>

<article class="abs rcard" style="left:0;width:156px">
  <div class="ph" role="img" aria-label="Pool pump and filter equipment" style="background:linear-gradient(160deg,#5aa6a0,#2f6f7c)"></div>
  <div class="badge" style="left:56px"><svg width="28" height="28" viewBox="0 0 28 28" fill="none" stroke="#fff" stroke-width="1.8"><rect x="5" y="8" width="15" height="9" rx="3"/><path d="M22 6v10a4 4 0 01-4 4h-3"/></svg></div>
  <div class="lbl" style="left:30px">Equipment</div>
</article>
<article class="abs rcard" style="left:174px;width:248px">
  <div class="ph" role="img" aria-label="Blue mosaic pool tiles" style="background:linear-gradient(150deg,#3d7ee0,#1f4fb8 60%,#9fd0ef)"></div>
  <div class="badge" style="left:156px"><svg width="30" height="30" viewBox="0 0 30 30" fill="none" stroke="#fff" stroke-width="1.8"><path d="M15 7l9 5-9 5-9-5zM6 17l9 5 9-5"/></svg></div>
  <svg class="back" width="30" height="12" viewBox="0 0 30 12"><path d="M29 6H2M7 1L2 6l5 5" stroke="#3b4b68" stroke-width="1.4" fill="none"/></svg>
  <div class="lbl" style="left:150px">Pool Tile</div>
</article>
<article class="abs rcard" style="left:442px;width:247px">
  <div class="ph" role="img" aria-label="Stone pool deck and hardscape beside a garden" style="background:linear-gradient(160deg,#6f8f55,#2e4f8a 60%,#c9ccc9)"></div>
  <div class="badge" style="left:148px"><svg width="30" height="30" viewBox="0 0 30 30" fill="none" stroke="#fff" stroke-width="1.8"><rect x="5" y="8" width="9" height="6"/><rect x="16" y="8" width="9" height="6"/><rect x="9" y="16" width="12" height="6"/></svg></div>
  <svg class="back" width="30" height="12" viewBox="0 0 30 12"><path d="M29 6H2M7 1L2 6l5 5" stroke="#3b4b68" stroke-width="1.4" fill="none"/></svg>
  <div class="lbl" style="left:96px">Hardscapes</div>
</article>

<div class="abs wash"></div>
<div class="abs tab on" style="left:145px"><span class="num">1</span>Why Choose Us?</div>
<div class="abs tab" style="left:455px"><span class="num">2</span>Build Process</div>
<div class="abs tab" style="left:765px"><span class="num">3</span>Financing</div>

<p class="abs center kick-c" style="top:1633px">Building concrete pools for a quarter-century!</p>
<h2 class="abs center h-sec" style="top:1672px">What Makes Us the Best Choice?</h2>

<div class="abs fbox" style="left:145px;top:1739px"><span class="big">25</span><h4>Two and a half decades of<br>Concrete Pool Building</h4><p>Hundreds of custom gunite pools built across the region.</p></div>
<div class="abs fbox" style="left:455px;top:1739px"><span class="big">3D</span><h4>3D Design Consult</h4><p>We model your pool, spa and hardscape in 3D so you can approve every detail first.</p></div>
<div class="abs fbox" style="left:765px;top:1739px"><span class="big">T</span><h4>Clear Build Timeline</h4><p>Design, permits, dig, steel, gunite, tile, plaster and fill, each step on a set schedule.</p></div>
<div class="abs fbox" style="left:145px;top:1900px"><span class="big">R</span><h4>Renovation &amp; Remodeling</h4><p>Resurfacing, new tile and coping, and modern equipment for older concrete pools.</p></div>
<div class="abs fbox" style="left:455px;top:1900px"><span class="big">L</span><h4>Repairs &amp; Liners</h4><p>Leak detection, crack repair and liner replacement handled by our own trained crews.</p></div>
<div class="abs fbox" style="left:765px;top:1900px"><span class="big">F</span><h4>Flexible Financing</h4><p>Low monthly payment plans so your new pool or remodel fits your budget.</p></div>

<section class="abs proj" role="img" aria-label="Muted blue backdrop of a finished concrete pool"></section>
<p class="abs center" style="top:2192px;font-size:11px;color:var(--cyan)">Featured projects</p>
<h2 class="abs center" style="top:2220px;font-size:24px;font-weight:500;color:#fff">Pool Designs &amp; Featured Pools</h2>
<div class="abs filters"><span class="on">All</span><span>New Builds</span><span>Renovations</span><span>Before &amp; After</span></div>

<article class="abs pcard" style="left:145px;top:2373px;width:299px;height:352px">
  <div class="abs" style="inset:0;background:linear-gradient(160deg,#3f8fc0,#2a6aa0)" role="img" aria-label="Newly built concrete backyard pool"></div>
  <div class="shade"></div>
  <div class="txt"><small>Baltimore, MD</small><h5>New Concrete Pool<br>Construction</h5><div class="price">$11500.00</div></div>
  <svg class="arr" width="32" height="14" viewBox="0 0 32 14"><path d="M1 7h29M25 2l5 5-5 5" stroke="#fff" stroke-width="1.4" fill="none"/></svg>
</article>
<article class="abs pcard" style="left:444px;top:2364px;width:321px;height:379px">
  <div class="abs" style="inset:0;background:linear-gradient(180deg,#9fd8f0 0%,#4c9a6a 35%,#2fb0d8 70%)" role="img" aria-label="Renovated pool shown after resurfacing"></div>
  <div class="shade"></div>
  <div class="txt"><small>Baltimore, MD</small><h5>Pool Renovation<br>Before &amp; After</h5><div class="price">$11500.00</div></div>
  <svg class="arr" width="32" height="14" viewBox="0 0 32 14"><path d="M1 7h29M25 2l5 5-5 5" stroke="#fff" stroke-width="1.4" fill="none"/></svg>
</article>
<article class="abs pcard" style="left:765px;top:2373px;width:290px;height:352px">
  <div class="abs" style="inset:0;background:linear-gradient(180deg,#b9dcef 0%,#5fa8d6 45%,#2a88c4 100%)" role="img" aria-label="Concrete infinity-edge pool overlooking water"></div>
  <div class="shade"></div>
  <div class="txt"><small>Baltimore, MD</small><h5>New Concrete Pool<br>Construction</h5><div class="price">$11500.00</div></div>
  <svg class="arr" width="32" height="14" viewBox="0 0 32 14"><path d="M1 7h29M25 2l5 5-5 5" stroke="#fff" stroke-width="1.4" fill="none"/></svg>
</article>

<div class="abs" style="left:145px;top:2921px;width:446px;height:399px;background:linear-gradient(180deg,#3f4f4a 0%,#2b4a55 45%,#1d6f8c 75%,#2a3f52 100%)" role="img" aria-label="Modern house beside a lit concrete pool at dusk"></div>
<article class="abs tcard">
  <h3>Amazing Build</h3>
  <p>From the 3D design to the final fill, our new concrete pool was finished on the timeline they promised.</p>
  <div class="who"><b>--Mara Quill</b>, Homeowner, Fairview</div>
</article>
<svg class="abs qmark" width="116" height="70" viewBox="0 0 116 70"><path d="M22 0h34L34 70H0zM78 0h38L94 70H56z" fill="#4c6189"/></svg>
<div class="abs tside"><small>Our testimonials</small><h2>What Our<br>Customers<br>Say About Us</h2></div>
<div class="abs dots"><i></i><i class="on"></i></div>

<div class="abs stat" style="left:221px;top:3506px"><div class="circ">20+</div><h6>Industry Awards</h6><p>Recognized for custom concrete pool design and craftsmanship.</p></div>
<div class="abs stat" style="left:470px;top:3506px"><div class="circ">99%</div><h6>Project Success</h6><p>Builds and remodels finished on schedule and on budget.</p></div>
<div class="abs stat" style="left:221px;top:3717px"><div class="circ">80+</div><h6>Employees</h6><p>Designers, builders, tile setters and finish crews in house.</p></div>
<div class="abs stat" style="left:470px;top:3717px"><div class="circ">15k+</div><h6>Happy Clients</h6><p>Families enjoying a new or renovated pool we built.</p></div>

<form class="abs quote">
  <h2>Get a <em>FREE</em> Quote</h2>
  <div class="field" style="left:45px;top:100px;width:279px">Your Name</div>
  <div class="field" style="left:45px;top:157px;width:130px">E-mail</div>
  <div class="field" style="left:194px;top:157px;width:130px">Phone</div>
  <div class="field" style="left:45px;top:215px;width:279px">Address</div>
  <div class="field" style="left:45px;top:273px;width:279px">Service: New Build, Renovation, Financing</div>
  <div class="field" style="left:45px;top:331px;width:130px">Date of visit</div>
  <div class="field" style="left:194px;top:331px;width:130px">Time of visit</div>
  <div class="submit">SUBMIT REQUEST</div>
</form>

<p class="abs center kick-c" style="top:4010px">Please Contact Us Today!</p>
<h2 class="abs center" style="top:4046px;font-size:25px;font-weight:500;color:var(--ink)">Are You Eager to Achieve Your Dream?</h2>
<div class="abs center" style="top:4120px"><p class="lead">Planning a new concrete pool or a full remodel of the one you have? Book a free design consult, see it in 3D and ask about our financing options.</p></div>
<div class="abs cta-phone">
  <svg width="28" height="28" viewBox="0 0 28 28"><circle cx="14" cy="14" r="13" fill="none" stroke="#17b4e6" stroke-width="1.4"/><path d="M10.5 12.3a8 8 0 003.7 3.7l1.3-1.3a.6.6 0 01.6-.15 6.5 6.5 0 002 .35.6.6 0 01.6.6v2a.6.6 0 01-.6.6 9.6 9.6 0 01-9.6-9.6.6.6 0 01.6-.6h2a.6.6 0 01.6.6c0 .7.1 1.4.35 2a.6.6 0 01-.15.6z" fill="none" stroke="#17b4e6" stroke-width="1.1"/></svg>
  0-(800)-555-01-42
</div>

<footer class="abs footer" role="img" aria-label="Muted blue backdrop of a pool deck"></footer>
<div class="abs ftab">
  <div class="brand">
    <div class="mark" style="width:28px;height:28px"></div>
    <div><div class="name" style="font-size:28px">Tidewell</div><div class="tag">CONCRETE POOL BUILDERS</div></div>
  </div>
</div>
<div class="abs fcol" style="left:145px;top:4434px;width:300px">
  <h4>About Us</h4>
  <p>We design, build and renovate custom concrete pools, from 3D modeling and financing to the final fill.</p>
  <div style="display:flex;gap:10px;margin-top:14px"><div class="soc"></div><div class="soc"></div></div>
</div>
<div class="abs fcol" style="left:531px;top:4434px"><h4>Quick Links</h4></div>
<div class="abs flinks" style="left:535px;top:4464px"><div>Home</div><div>New Builds</div><div>Renovations</div><div>Financing</div></div>
<div class="abs flinks" style="left:693px;top:4464px"><div>Gallery</div><div>Before &amp; After</div><div>Build Process</div><div>Contacts</div></div>
<div class="abs fcol" style="left:843px;top:4434px">
  <h4>Contacts</h4>
  <div class="fcontact">1270 Larkspur Lane Fairview, VA<br>United States<br>mail: <span style="font-weight:400">info@tidewell.com</span><br>0 (800) 555 01 42</div>
</div>
<p class="abs copy">© 2023 Tidewell. All Rights Reserved. – Terms &amp; Conditions – Privacy Policy</p>

</body>
</html>
```